Havenry - "Where Pest Control is Free for Life..." Please see pitch deck...

Project goal, that this is a reusable template, not a one-off card
Brand and design direction, follow the logo, use the brand palette (with a color swatch table), typography and layout guidance
The Mark Vale placeholder content as a clean field-by-field table (name, title, company, address, office, cell, fax, email, havenry.com)
Print specs, 3.5 × 2 in trim, 0.125 in bleed, 300 DPI, CMYK, crop marks
Deliverables, layered editable PSD (your primary ask) plus vector .AI/.EPS and a press-ready PDF/X-1a, with fonts packaged
What you'll provide (logo, colors, fonts)
Process and sign-off, concept first, then full file package on approval.
Populate every field with this Mark Vale placeholder data so we can see the layout fully built out. We will replace it per person.
Name Mark Vale
Title Title / Position
Company Havenry
Address 487 Orchard Lane, Suite 210, Tallahassee, FL 32308
Office (850) 555-0142
Cell (850) 555-0167
Fax (850) 555-0181
Email markvale@havenry.com
Website havenry.com

We need the working, editable source files so we can update them ourselves, plus a ready-to-print export:
1. Photoshop (.PSD) — fully layered and editable, with each contact field on its own labeled text layer. This is the primary requested format.
2. Vector source — the press-standard editable format, Adobe Illustrator (.AI) and/or .EPS, since vector is preferred for crisp text and logos at print.
3. Print-ready PDF — press-quality (PDF/X-1a), CMYK, with bleed and crop marks, both sides.
4. Packaged fonts and links — include or list all fonts used, and package any linked assets so the files open correctly on our end.

Why both PSD and vector
The PSD covers our request directly and is easy for us to edit. Vector (.AI/.EPS) is what most commercial printers actually prefer for type and logos because it stays razor-sharp at any size. Providing both keeps us flexible no matter which printer we use. Have fun and keep it modern and cool the designer of the logo did a great job, see what you can do.

```html
<!DOCTYPE html>
<html lang="en">
<head>
<meta charset="utf-8">
<title>Havenry — Business Card</title>
<link href="https://fonts.googleapis.com/css2?family=Montserrat:wght@400;600;700;800&family=Lato:wght@400;700&display=swap" rel="stylesheet">
<style>
  :root {
    --stage: #141414;
    --card: #1b1b1c;
    --teal: #0fb3c6;
    --white: #ffffff;
    --ink: #e9e9e9;
    --band-ink: #16191a;
    --back-dark: #0c0c0c;
    --back-light: #4a4a4a;
  }
  * { box-sizing: border-box; margin: 0; padding: 0; }
  html, body {
    width: 1200px; height: 1059px; overflow: hidden;
    background: var(--stage);
  }
  .stage { position: relative; width: 1200px; height: 1059px; }

  .card {
    position: absolute; left: 255px; width: 690px; height: 394px;
    border-radius: 22px; overflow: hidden;
  }
  .card--front { top: 87px; background: var(--card); }
  .card--back {
    top: 557px;
    background: linear-gradient(90deg, var(--back-dark) 0%, #111 50%, #2a2a2a 72%, var(--back-light) 100%);
  }

  .brand-name {
    position: absolute; right: 26px; top: 46px;
    font-family: 'Montserrat', sans-serif; font-weight: 800;
    font-size: 62px; letter-spacing: -1.5px; line-height: 1;
    color: var(--white);
  }

  .person { position: absolute; left: 37px; top: 182px; }
  .person__name {
    font-family: 'Montserrat', sans-serif; font-weight: 700;
    font-size: 27px; letter-spacing: 0.5px; color: var(--teal); line-height: 1.1;
  }
  .person__title {
    font-family: 'Montserrat', sans-serif; font-weight: 400;
    font-size: 19px; color: var(--ink); margin-top: 2px;
  }

  .divider {
    position: absolute; left: 31px; top: 251px; width: 634px; height: 2px;
    background: var(--ink);
  }

  .contact {
    position: absolute; display: flex; align-items: center; gap: 8px;
    font-family: 'Lato', sans-serif; font-size: 19px; color: var(--ink);
    white-space: nowrap;
  }
  .contact svg { width: 18px; height: 18px; fill: var(--teal); flex: none; }
  .contact--office { left: 31px; top: 266px; }
  .contact--cell   { left: 31px; top: 298px; }
  .contact--fax    { left: 216px; top: 264px; }
  .contact--email  { left: 216px; top: 296px; }
  .contact--email svg { margin-right: 8px; }
  .contact--address { left: 31px; top: 330px; }

  .band { position: absolute; left: 0; top: 0; width: 690px; height: 394px; }
  .band__url {
    position: absolute; left: 560px; top: 365px; transform: translateX(-50%);
    font-family: 'Lato', sans-serif; font-size: 18px; line-height: 28px;
    color: var(--band-ink);
  }

  .back-pattern { position: absolute; inset: 0; }
</style>
</head>
<body>
<main class="stage">

  <section class="card card--front">
    <svg class="band" viewBox="0 0 690 394" aria-hidden="true">
      <polygon fill="#0fb3c6" points="416,365 690,365 690,394 0,394 0,386 392,386"/>
      <polygon fill="#0fb3c6" points="0,372 404,372 397,381 0,381"/>
    </svg>

    <div class="brand-name">Havenry</div>

    <div class="person">
      <h1 class="person__name">MARK VALE</h1>
      <p class="person__title">Owner</p>
    </div>

    <div class="divider"></div>

    <p class="contact contact--office">
      <svg viewBox="0 0 24 24"><path d="M2 9c0-3 5-5 10-5s10 2 10 5v2h-5V8.5c-1.5-.6-3.3-.9-5-.9s-3.5.3-5 .9V11H2z"/><path d="M6 12l2-3h8l2 3v8H6z"/><rect x="10" y="13" width="4" height="4" fill="#1b1b1c"/></svg>
      (850) 555-0142
    </p>
    <p class="contact contact--cell">
      <svg viewBox="0 0 24 24"><path d="M7 1h10a2 2 0 0 1 2 2v18a2 2 0 0 1-2 2H7a2 2 0 0 1-2-2V3a2 2 0 0 1 2-2zm0 3v14h10V4z"/><circle cx="12" cy="20.5" r="1.2" fill="#1b1b1c"/></svg>
      (850) 555-0167
    </p>
    <p class="contact contact--fax">
      <svg viewBox="0 0 24 24"><rect x="1" y="6" width="5" height="16" rx="1"/><path d="M8 8h15v14H8z"/><rect x="11" y="2" width="9" height="5"/><g fill="#1b1b1c"><rect x="11" y="10" width="9" height="3"/><rect x="11" y="15" width="2" height="2"/><rect x="15" y="15" width="2" height="2"/><rect x="11" y="18" width="2" height="2"/><rect x="15" y="18" width="2" height="2"/></g></svg>
      (850) 555-0181
    </p>
    <p class="contact contact--email">
      <svg viewBox="0 0 24 24"><path d="M1 5h22v14H1z"/><path d="M1.5 5.5 12 13l10.5-7.5" fill="none" stroke="#1b1b1c" stroke-width="2"/></svg>
      markvale@havenry.com
    </p>
    <p class="contact contact--address">
      <svg viewBox="0 0 24 24"><path d="M12 1a8 8 0 0 0-8 8c0 6 8 14 8 14s8-8 8-14a8 8 0 0 0-8-8zm0 11a3 3 0 1 1 0-6 3 3 0 0 1 0 6z"/></svg>
      487 Orchard Lane, Suite 210, Tallahassee, FL 32308
    </p>

    <p class="band__url">www.havenry.com</p>
  </section>

  <section class="card card--back">
    <div class="back-pattern" role="img" aria-label="Repeating tiled pattern of the brand's house symbol, fading from black to grey, with one tile highlighted in teal"></div>
  </section>

</main>
</body>
</html>
```